Event Flyer - LGBT Camping Event

I have attached a poster I made (SampleFlyer.pdf) that has all the elements I want. Just don't like the layout and how things look. You can use any colors that make the poster work. I would like to incorporate the Campfest logo into the flyer (uploaded). You are welcome to grab elements from the event website to incorporate into your design (www.campfestmeadowlark.org). I included a couple of pictures to possibly use too. Please include all 8 sponsors and the two hosts are the logos on the bottom of sample flyer - Prairie Alliance & Pinecrest Trail Council. The flyer size needs to be 12"Wide x 17" Tall. Here is a dropbox link to a possible image to use. https://lnk.example/7qTzKwd

Please use the wording;

DON’T MISS this LGBT camping event!

Plan the highlight of your summer TODAY.

It’s almost time for the Rocky Mountain Region’s largest LGBT pride camping event: Campfest Meadowlark!
Join us August 8th-12th for 5 days of fun in a friendly, safe, LGBT affirming environment for everyone, from everywhere!

More Info or Register Online www.sagebrightfest.org

Target Market(s)

LGBT Campers

Industry/Entity Type

Event

Colors

Designer to choose colors to be used in the design.

Requirements
Must have
• Must have text outlined in project description, Campfest logo, sponsor logos and host logos.

```html
<!DOCTYPE html>
<html lang="en">
<head>
<meta charset="utf-8">
<title>Campfest Meadowlark – LGBT Camping Event Flyer</title>
<link href="https://fonts.googleapis.com/css2?family=Fira+Sans:wght@500;600;700&display=swap" rel="stylesheet">
<style>
  :root {
    --page-bg: #dcdce6;
    --forest: #0b5e2a;
    --forest-dark: #0a4a20;
    --sun: #f6ef6a;
    --gold-text: #f7ec5a;
    --white: #ffffff;
    --ink: #1a1a1a;
    --navy: #1f3a6b;
    --teal: #1a8fbf;
  }
  * { box-sizing: border-box; margin: 0; padding: 0; }
  html, body { width: 1200px; height: 1200px; overflow: hidden; background: var(--page-bg); }
  body { font-family: "Fira Sans", Arial, sans-serif; }

  .flyer {
    position: absolute; left: 177px; top: 0;
    width: 846px; height: 1200px;
    background: var(--white); overflow: hidden;
  }

  .hero { position: absolute; left: 0; top: 0; width: 846px; height: 692px; }
  .hero-photo {
    position: absolute; inset: 0;
    background:
      linear-gradient(180deg, #0f6a2c 0%, #1e6a32 18%, rgba(30,90,45,0) 30%),
      radial-gradient(ellipse at 65% 45%, #b47a3e 0%, #7a4a28 35%, rgba(0,0,0,0) 60%),
      linear-gradient(90deg, #5a6f8c 0%, #2c3f78 30%, #3a5f8f 55%, #c0563e 78%, #2e4f8c 100%);
  }
  .hero-headline {
    position: absolute; top: 30px; left: 0; width: 100%;
    text-align: center; color: var(--white);
  }
  .hero-headline h1 { font-size: 38px; font-weight: 700; letter-spacing: 0.3px; }
  .hero-headline p { font-size: 32px; font-weight: 500; margin-top: 12px; }

  .details {
    position: absolute; left: 0; top: 692px; width: 846px; height: 187px;
    background: var(--forest); color: var(--white); text-align: center;
    padding: 18px 28px 0;
  }
  .details-body { font-size: 21px; font-weight: 600; line-height: 1.5; }
  .details-meta {
    display: flex; justify-content: center; gap: 48px;
    margin-top: 14px; color: var(--gold-text); font-size: 23px; font-weight: 600;
  }

  .sponsors-bar {
    position: absolute; left: 0; top: 879px; width: 846px; height: 48px;
    background: var(--sun); color: var(--forest);
    font-size: 22px; font-weight: 600; text-align: center; line-height: 48px;
  }

  .sponsor {
    position: absolute; transform: translate(-50%, -50%);
    display: flex; align-items: center; gap: 8px;
    font-weight: 700; white-space: nowrap; text-align: center;
  }
  .sponsor .mark { width: 14px; height: 14px; flex: none; }
  .sponsor--host { font-size: 26px; }
  .sponsor--host .mark { width: 22px; height: 22px; }
  .sponsor--regular { font-size: 19px; }
  .sponsor--tile {
    background: var(--ink); color: var(--white);
    font-size: 14px; line-height: 1.25; padding: 8px 12px;
    display: block; white-space: normal;
  }
  .c-teal { color: var(--teal); }
  .c-navy { color: var(--navy); }
  .c-forest { color: var(--forest); }
  .c-ink { color: var(--ink); }
</style>
</head>
<body>
  <main class="flyer">
    <section class="hero">
      <div class="hero-photo" role="img" aria-label="Photo of two smiling men relaxing together by a tent in a sunlit pine forest"></div>
      <div class="hero-headline">
        <h1>DON’T MISS THIS LGBT CAMPING EVENT !</h1>
        <p>Plan the highlight of your summer today.</p>
      </div>
    </section>

    <section class="details">
      <p class="details-body">It’s almost time for the Rocky Mountain Region’s largest LGBT pride camping event: Campfest Meadowlark! Join us for 5 days of fun in a friendly, safe, LGBT affirming environment for everyone, from everywhere!</p>
      <div class="details-meta">
        <span>August 8th-12th</span>
        <span>More Info or Register Online www.sagebrightfest.org</span>
      </div>
    </section>

    <div class="sponsors-bar">OUR SPONSORS</div>

    <section class="sponsor-grid">
      <div class="sponsor sponsor--host c-teal" style="left:138px; top:984px;">
        <svg class="mark" viewBox="0 0 10 10"><rect width="10" height="10" fill="var(--teal)"/></svg>Prairie Alliance
      </div>
      <div class="sponsor sponsor--host c-forest" style="left:427px; top:984px; font-size:22px;">
        <svg class="mark" viewBox="0 0 10 10"><circle cx="5" cy="5" r="5" fill="var(--forest)"/></svg>Pinecrest Trail Council
      </div>
      <div class="sponsor sponsor--host c-navy" style="left:698px; top:984px;">
        <svg class="mark" viewBox="0 0 10 10"><circle cx="5" cy="5" r="5" fill="var(--navy)"/></svg>Campfest
      </div>

      <div class="sponsor sponsor--regular c-ink" style="left:119px; top:1078px;">Open Circle Alpine</div>
      <div class="sponsor sponsor--regular c-navy" style="left:322px; top:1078px;">Harlan Wells</div>
      <div class="sponsor sponsor--regular c-ink" style="left:548px; top:1078px;">trailnote.org</div>
      <div class="sponsor sponsor--regular c-teal" style="left:734px; top:1078px;">Dottie’s Summit</div>

      <div class="sponsor sponsor--tile" style="left:94px; top:1149px;">Zed<br>Lounge</div>
      <div class="sponsor sponsor--tile" style="left:288px; top:1149px;">Sweetwater<br>Physical Therapy</div>
      <div class="sponsor sponsor--tile" style="left:517px; top:1149px;">Dell’s Roadside<br>Bar and Grill</div>
      <div class="sponsor sponsor--tile" style="left:729px; top:1149px;">Juno’s<br>Ministores</div>
    </section>
  </main>
</body>
</html>
```